Lawyer Needs New Atypical Stationery Design With Gravitas

I need new stationery (letterhead, envelopes, note pads, maybe business cards) for my law office. Although I work by myself, for myself, I need stationery that conveys strength, stability, and gravitas. I would also like a design that makes the end user think: "This is unique. I've never seen letterhead like this before." Most importantly, it should not look like many lawyers' letterhead, meaning no scales of justice. My current letterhead (attached) has my name and "Attorney at Law" on it; however, I would like to transition to "MERIX | LAW" or something like that with the new letterhead. Lastly, I would like an envelope design that is not the standard #10 envelope with a triangular back flap, maybe a square flap or something in the style or design that also makes people stop and think "That's different from anything I've seen before."

```html
<!DOCTYPE html>
<html lang="en">
<head>
<meta charset="utf-8">
<title>Merix Law — Business Cards</title>
<link rel="stylesheet" href="https://fonts.googleapis.com/css2?family=Poppins:wght@400;500;700&display=swap">
<style>
  :root {
    --canvas-bg: #efece6;
    --card-white: #ffffff;
    --brand-blue: #243f99;
    --brand-blue-light: #4a63b8;
    --ink: #1b1b1f;
    --card-shadow: 0 10px 24px rgba(40, 35, 25, 0.18);
  }
  * { box-sizing: border-box; margin: 0; padding: 0; }
  html, body {
    width: 1200px;
    height: 840px;
    overflow: hidden;
    background: var(--canvas-bg);
    font-family: "Poppins", sans-serif;
  }
  .stage {
    position: relative;
    width: 1200px;
    height: 840px;
    display: flex;
    align-items: center;
    justify-content: center;
    gap: 70px;
  }
  .card {
    width: 400px;
    height: 400px;
    box-shadow: var(--card-shadow);
  }
  .card-front {
    background: var(--card-white);
    display: flex;
    flex-direction: column;
    align-items: center;
    padding: 36px 30px 30px;
    text-align: center;
    color: var(--ink);
  }
  .brand-name {
    display: flex;
    align-items: center;
    gap: 12px;
    font-weight: 500;
    font-size: 34px;
    letter-spacing: 2px;
    color: var(--brand-blue);
    line-height: 1;
  }
  .brand-square {
    width: 16px;
    height: 16px;
    background: var(--brand-blue);
  }
  .person-name {
    margin-top: 26px;
    font-weight: 700;
    font-size: 22px;
    letter-spacing: 0.5px;
    color: var(--brand-blue);
    line-height: 1.1;
  }
  .person-title {
    font-size: 12px;
    color: var(--ink);
    margin-top: 2px;
  }
  .address {
    margin-top: 12px;
    font-size: 12.5px;
    line-height: 1.45;
    text-transform: uppercase;
    letter-spacing: 0.3px;
  }
  .icon-rule {
    margin-top: 12px;
    display: flex;
    align-items: center;
    gap: 8px;
  }
  .icon-rule .rule {
    width: 52px;
    height: 1.5px;
    background: var(--brand-blue);
  }
  .icon-rule svg { display: block; }
  .contact {
    margin-top: 12px;
    font-size: 13px;
    line-height: 1.5;
    letter-spacing: 0.3px;
  }
  .card-back {
    background: var(--brand-blue);
    position: relative;
  }
  .back-mark {
    position: absolute;
    left: 50%;
    top: 50%;
    transform: translate(-50%, -50%) rotate(90deg);
    font-weight: 500;
    font-size: 34px;
    letter-spacing: 2px;
    color: var(--brand-blue-light);
    white-space: nowrap;
  }
</style>
</head>
<body>
  <main class="stage">
    <section class="card card-front" aria-label="Business card front">
      <div class="brand-name"><span class="brand-square"></span>MERIX LAW</div>
      <h1 class="person-name">DANIEL HART</h1>
      <p class="person-title">Managing Director</p>
      <p class="address">4120 Alder Avenue<br>Suite Three Hundred<br>Lakeview, CA 90300-1180</p>
      <div class="icon-rule">
        <span class="rule"></span>
        <svg width="18" height="18" viewBox="0 0 18 18" aria-label="Phone">
          <circle cx="9" cy="9" r="9" fill="var(--brand-blue)"/>
          <path d="M6 5.2c.4-.3.9-.2 1.1.2l.7 1.3c.2.4.1.8-.2 1l-.5.4c.4.9 1.1 1.6 2 2l.4-.5c.3-.3.7-.4 1-.2l1.3.7c.4.2.5.7.2 1.1l-.5.6c-.5.5-1.3.6-1.9.3-1.8-.9-3.2-2.3-4.1-4.1-.3-.6-.2-1.4.3-1.9z" fill="#fff"/>
        </svg>
        <svg width="18" height="18" viewBox="0 0 18 18" aria-label="Email">
          <circle cx="9" cy="9" r="9" fill="var(--brand-blue)"/>
          <rect x="4.5" y="6" width="9" height="6.2" rx="0.6" fill="#fff"/>
          <path d="M4.8 6.3 9 9.4l4.2-3.1" fill="none" stroke="var(--brand-blue)" stroke-width="0.9"/>
        </svg>
        <svg width="18" height="18" viewBox="0 0 18 18" aria-label="Website">
          <circle cx="9" cy="9" r="9" fill="var(--brand-blue)"/>
          <circle cx="9" cy="9" r="4.3" fill="none" stroke="#fff" stroke-width="1"/>
          <ellipse cx="9" cy="9" rx="1.8" ry="4.3" fill="none" stroke="#fff" stroke-width="0.9"/>
          <line x1="4.7" y1="9" x2="13.3" y2="9" stroke="#fff" stroke-width="0.9"/>
        </svg>
        <span class="rule"></span>
      </div>
      <p class="contact">(555) 014-2700<br>INFO@MERIXLAW.COM<br>WWW.MERIXLAW.COM</p>
    </section>

    <section class="card card-back" aria-label="Business card back">
      <div class="back-mark">MERIX LAW</div>
    </section>
  </main>
</body>
</html>
```